Financial Dashboard UI design

We are building a financial dashboard for business management teams, and would like a futuristic and sophisticated design (light and dark themes).

There are a total of 3 screens (attached images: nemo1, nemo2, nemo3).
nemo1 image is comprised of 6 scorecards (attached image: scorecard)
This will also need a design.

So, I'm expecting 4 UI designs in total.

I've added some example UI for inspiration. (sample1 , sample2, sample3, sample4).

Thanks

```html
<!DOCTYPE html>
<html lang="en">
<head>
<meta charset="utf-8">
<title>2021 U.S Sales – Report</title>
<link href="https://fonts.googleapis.com/css2?family=Roboto:wght@400;500;700&display=swap" rel="stylesheet">
<style>
  :root {
    --page-bg: #2e3250;
    --nav-bg: #646a99;
    --nav-active: #7c85b8;
    --band-bg: #4a5180;
    --cell-bg: #4a5180;
    --cell-dark: #333a64;
    --grid-line: #7078b2;
    --head-bg: #d45f6e;
    --text: #ffffff;
    --text-soft: #e6e8f3;
    --good-fill: #a2cf48;
    --bad-fill: #ff0000;
    --good-text: #c9f22a;
  }
  * { box-sizing: border-box; margin: 0; padding: 0; }
  html, body { width: 1200px; height: 849px; overflow: hidden; }
  body {
    background: var(--page-bg);
    font-family: "Roboto", sans-serif;
    color: var(--text);
    position: relative;
  }
  .brand { position: absolute; left: 21px; top: 10px; width: 210px; text-align: center; }
  .brand-dot { display: block; width: 38px; height: 38px; border-radius: 50%; background: var(--text); margin: 0 auto 2px 84px; }
  .brand-name { font-size: 36px; font-weight: 400; letter-spacing: 0.2px; white-space: nowrap; text-align: left; }
  .report-title { position: absolute; right: 482px; top: 22px; text-align: right; }
  .report-title h1 { font-size: 35px; font-weight: 700; line-height: 1.1; }
  .report-title p { font-size: 16px; margin-top: 6px; color: var(--text-soft); }
  .elements { position: absolute; right: 19px; top: 18px; text-align: right; width: 460px; }
  .elements h2 { font-size: 21px; font-weight: 500; margin-bottom: 6px; }
  .elements p { font-size: 15.5px; line-height: 25px; color: var(--text-soft); }
  .panel { position: absolute; left: 21px; top: 116px; width: 1158px; }
  .nav {
    height: 45px; background: var(--nav-bg);
    border-radius: 17px 17px 0 0; display: flex; align-items: stretch; overflow: hidden;
    font-size: 16px; font-weight: 500;
  }
  .nav a { color: var(--text-soft); text-decoration: none; display: flex; align-items: center; padding: 0 10px; }
  .nav a.active { background: var(--nav-active); width: 88px; padding-left: 21px; margin-right: 0; }
  .band { height: 19px; background: var(--band-bg); }
  .band.bottom { height: 17px; border-radius: 0 0 14px 14px; }
  table { width: 1158px; border-collapse: collapse; table-layout: fixed; font-size: 12.5px; }
  th, td { text-align: right; padding-right: 7px; border: 1px solid var(--grid-line); white-space: nowrap; overflow: hidden; }
  th { background: var(--head-bg); height: 40px; font-size: 15.5px; font-weight: 500; padding-right: 6px; }
  td { background: var(--cell-bg); height: 40.9px; }
  td.country { background: var(--cell-dark); padding-right: 4px; }
  td.good { background: var(--good-fill); }
  td.bad { background: var(--bad-fill); }
  td.up { color: var(--good-text); }
</style>
</head>
<body>
  <div class="brand">
    <span class="brand-dot"></span>
    <div class="brand-name">Financial App</div>
  </div>

  <div class="report-title">
    <h1>2021 U.S Sales</h1>
    <p>Page 1/107 (2886 records)</p>
  </div>

  <div class="elements">
    <h2>Available Elements:</h2>
    <p>Lorem ipsum dolor sit amet, consectetur adipiscing elit, sed do<br>eiusmod tempor incididunt ut labore et dolore magna aliqua.</p>
  </div>

  <div class="panel">
    <nav class="nav">
      <a class="active">Report</a>
      <a>Charts</a><a>Email</a><a>Calendar</a><a>Notifications</a><a>Stand-in</a>
      <a>Tasks</a><a>Market</a><a>News</a><a>Search</a><a>Glossary</a><a style="padding-left:14px">Settings</a>
    </nav>
    <div class="band"></div>
    <table class="sales">
      <colgroup>
        <col style="width:157px"><col style="width:110px"><col style="width:145px"><col style="width:139px">
        <col style="width:49px"><col style="width:119px"><col style="width:150px"><col style="width:45px">
        <col style="width:147px"><col style="width:97px">
      </colgroup>
      <thead>
        <tr><th>Styleindex</th><th>Country</th><th>Business Area</th><th>Actual</th><th>Pla</th><th>Forecast</th><th>Total</th><th>right</th><th>IT Sub Area</th><th>Same</th></tr>
      </thead>
      <tbody>
        <tr><td>Administration</td><td class="country">Germany</td><td>Distribution</td><td class="up">50598.8</td><td>0</td><td>0</td><td class="good">2560965547.63</td><td>ny</td><td>Administration</td><td class="up">50708</td></tr>
        <tr><td>Administration</td><td class="country">Germany</td><td>Distribution</td><td>0</td><td>0</td><td>0</td><td class="good">2560965547.63</td><td>ny</td><td>Administration</td><td class="up">50708</td></tr>
        <tr><td>Administration</td><td class="country">Germany</td><td>Distribution</td><td>0</td><td>0</td><td>0</td><td class="good">2560965547.63</td><td>ny</td><td>Administration</td><td class="up">50708</td></tr>
        <tr><td>Administration</td><td class="country">Germany</td><td>Distribution</td><td>613.81</td><td>0</td><td>0</td><td class="good">2560965547.63</td><td>ny</td><td>Administration</td><td class="up">50708</td></tr>
        <tr><td>Administration</td><td class="country">Germany</td><td>Distribution</td><td class="up">11061.1</td><td>0</td><td>0</td><td class="good">2560965547.63</td><td>ny</td><td>Administration</td><td class="up">50708</td></tr>
        <tr><td>Administration</td><td class="country">Germany</td><td>Distribution</td><td class="up">17978.25</td><td>0</td><td>0</td><td class="good">2560965547.63</td><td>ny</td><td>Administration</td><td class="up">50708</td></tr>
        <tr><td>Administration</td><td class="country">Germany</td><td>Distribution</td><td>255</td><td>0</td><td>0</td><td class="good">2560965547.63</td><td>ny</td><td>Administration</td><td class="up">50708</td></tr>
        <tr><td>Administration</td><td class="country">Germany</td><td>Distribution</td><td>2012</td><td>0</td><td>0</td><td class="good">2560965547.63</td><td>ny</td><td>Administration</td><td class="bad">-55815</td></tr>
        <tr><td>Administration</td><td class="country">Germany</td><td>Distribution</td><td>68493.91</td><td>0</td><td>0</td><td class="good">2560965547.63</td><td>ny</td><td>Administration</td><td class="bad">-10540</td></tr>
        <tr><td>Administration</td><td class="country">Germany</td><td>Distribution</td><td>655</td><td>0</td><td>0</td><td class="bad">-144.57</td><td>ny</td><td>Administration</td><td class="up">50708</td></tr>
        <tr><td>Administration</td><td class="country">Germany</td><td>Distribution</td><td class="up">0</td><td>0</td><td>0</td><td class="good">2560965547.63</td><td>ny</td><td>Administration</td><td class="bad">-8428</td></tr>
        <tr><td>Administration</td><td class="country">Germany</td><td>Distribution</td><td>115</td><td>0</td><td>0</td><td class="good">2560965547.63</td><td>ny</td><td>Administration</td><td class="up">50708</td></tr>
        <tr><td>Administration</td><td class="country">Germany</td><td>Distribution</td><td>55925.7</td><td>0</td><td>0</td><td class="good">2560965547.63</td><td>ny</td><td>Administration</td><td class="up">50708</td></tr>
        <tr><td>Administration</td><td class="country">Germany</td><td>Distribution</td><td class="up">0</td><td>0</td><td>0</td><td class="good">2560965547.63</td><td>ny</td><td>Administration</td><td class="up">50708</td></tr>
      </tbody>
    </table>
    <div class="band bottom"></div>
  </div>
</body>
</html>
```